Modern Business Card Design
Consulting firm - Engineering/Infrastructure Sector
Use same font as used in my logo
but we are open to new fonts, as long as the printer will not have trouble with them.
Professional
Melanie Trovaskis
Partner
4215 Linwood Avenue
Suite 207
mtrovaskis@brightholmpx.com
www.brightholmpx.com
we're looking for something sharp and complementary to our logo

```html
<!DOCTYPE html>
<html lang="en">
<head>
<meta charset="utf-8">
<title>Brightholm Business Card</title>
<link href="https://fonts.googleapis.com/css2?family=Cinzel:wght@400;600&display=swap" rel="stylesheet">
<style>
  :root {
    --bg: #e4e5e7;
    --card: #ffffff;
    --navy: #1d3b8c;
    --sky: #5cb6e6;
    --sky-pale: #d7ecf8;
    --ink: #2a3f7a;
  }
  * { margin: 0; padding: 0; box-sizing: border-box; }
  html, body { width: 1200px; height: 984px; overflow: hidden; }
  body {
    background: var(--bg);
    font-family: "Cinzel", "Times New Roman", serif;
    color: var(--ink);
    position: relative;
  }
  .card {
    position: absolute;
    left: 250px;
    width: 700px;
    height: 400px;
    background: var(--card);
    border-radius: 22px;
    overflow: hidden;
    box-shadow: 0 10px 28px rgba(0,0,0,0.18);
  }
  .card-back { top: 80px; }
  .card-front { top: 520px; }

  /* back */
  .back-circle {
    position: absolute;
    right: 70px; top: 70px;
    width: 250px; height: 250px;
    border-radius: 50%;
    background: radial-gradient(circle at 40% 35%, #f2f8fd, var(--sky-pale));
    opacity: 0.8;
  }
  .back-web {
    position: absolute;
    left: 60px; top: 186px;
    font-size: 22px;
    letter-spacing: 3px;
    color: var(--navy);
  }

  /* front */
  .brand {
    position: absolute;
    left: 60px; top: 40px;
    display: flex; align-items: center; gap: 18px;
  }
  .brand-mark {
    width: 74px; height: 74px; border-radius: 50%;
    background: var(--sky);
  }
  .brand-name {
    font-size: 44px; font-weight: 600;
    color: var(--navy); letter-spacing: 2px;
  }
  .person {
    position: absolute;
    left: 40px; top: 152px; width: 310px;
    text-align: right;
  }
  .person-name { font-size: 25px; color: var(--navy); letter-spacing: 0.5px; }
  .person-role { font-size: 15px; margin-top: 4px; letter-spacing: 1px; }
  .address { margin-top: 22px; font-size: 16px; line-height: 1.35; letter-spacing: 0.5px; }

  .contacts {
    position: absolute;
    left: 372px; top: 158px;
    list-style: none;
    font-size: 14px; letter-spacing: 0.5px;
  }
  .contacts li { display: flex; align-items: center; gap: 9px; height: 21px; }
  .icon { width: 15px; height: 15px; flex: none; }

  .waves { position: absolute; left: 0; bottom: 0; width: 700px; height: 150px; }
</style>
</head>
<body>
  <section class="card card-back">
    <div class="back-circle"></div>
    <p class="back-web">www.brightholmpx.com</p>
  </section>

  <section class="card card-front">
    <header class="brand">
      <div class="brand-mark"></div>
      <span class="brand-name">BRIGHTHOLM</span>
    </header>

    <div class="person">
      <h1 class="person-name">Melanie Trovaskis</h1>
      <p class="person-role">Partner</p>
      <p class="address">4215 Linwood Avenue<br>Suite 207</p>
    </div>

    <ul class="contacts">
      <li><svg class="icon" viewBox="0 0 16 16"><circle cx="8" cy="8" r="8" fill="var(--navy)"/><path d="M5 4.5l2 0 .6 2-1 .8a5 5 0 0 0 2 2l.8-1 2 .6v2a1 1 0 0 1-1 1A7 7 0 0 1 4 5.5a1 1 0 0 1 1-1z" fill="#fff"/></svg>301.555.0142</li>
      <li><svg class="icon" viewBox="0 0 16 16"><circle cx="8" cy="8" r="8" fill="var(--navy)"/><rect x="5.5" y="3.5" width="5" height="9" rx="1" fill="#fff"/></svg>202.555.0186</li>
      <li><svg class="icon" viewBox="0 0 16 16"><circle cx="8" cy="8" r="8" fill="var(--navy)"/><rect x="4" y="6" width="8" height="5" fill="#fff"/><rect x="5.5" y="4" width="5" height="2" fill="#fff"/></svg>301.555.0173</li>
      <li><svg class="icon" viewBox="0 0 16 16"><circle cx="8" cy="8" r="8" fill="var(--navy)"/><rect x="4" y="5" width="8" height="6" fill="#fff"/><path d="M4 5l4 3.5L12 5" stroke="var(--navy)" fill="none"/></svg>mtrovaskis@brightholmpx.com</li>
      <li><svg class="icon" viewBox="0 0 16 16"><circle cx="8" cy="8" r="8" fill="var(--navy)"/><circle cx="8" cy="8" r="4" fill="none" stroke="#fff"/><path d="M4 8h8M8 4v8" stroke="#fff"/></svg>www.brightholmpx.com</li>
    </ul>

    <svg class="waves" viewBox="0 0 700 150" preserveAspectRatio="none">
      <path d="M0 40 C150 10 260 80 420 95 C540 105 630 95 700 80 L700 150 L0 150 Z" fill="var(--sky)"/>
      <path d="M0 60 C150 35 260 100 420 112 C540 120 630 112 700 100 L700 150 L0 150 Z" fill="#ffffff"/>
      <path d="M0 75 C150 55 260 115 420 125 C540 132 630 126 700 115 L700 150 L0 150 Z" fill="var(--navy)"/>
    </svg>
  </section>
</body>
</html>
```